Meridane Works, Inc. - Update our Website

Meridane Works needs a website to help our customers to navigate through our services efficiently. Our existing website is at www.meridwork.example

We would like to explain our services with content and pictures (photographs) that distinguishes our products and services from our competition.

The website design must implement a strategy to focus on our Contract Labeling services.

With this new design we would like to attract new customers and ensure that our existing customers are fully informed with our latest offerings.

```html
<!DOCTYPE html>
<html lang="en">
<head>
<meta charset="utf-8">
<title>Meridane Works, Inc.</title>
<link href="https://fonts.googleapis.com/css2?family=Krona+One&family=Roboto:wght@400;500;700&display=swap" rel="stylesheet">
<style>
:root{
  --blue:#0a6aa6;
  --blue-light:#3a8fc0;
  --orange:#ff7a00;
  --orange-light:#f7a04a;
  --green:#6cbf14;
  --green-light:#93c94a;
  --ink:#111;
  --text:#555;
  --footer:#0b0b0b;
  --field:#3a3a3a;
  --white:#fff;
}
*{box-sizing:border-box;margin:0;padding:0}
html,body{width:1200px;height:2304px;overflow:hidden;background:var(--white)}
body{font-family:"Roboto",sans-serif;color:var(--text);position:relative}
.abs{position:absolute}
h1,h2,h3,.display{font-family:"Krona One",sans-serif;text-transform:uppercase;font-weight:400}

/* header */
.brand{left:173px;top:22px;display:flex;align-items:center;gap:16px}
.brand-dot{width:62px;height:62px;border-radius:50%;background:var(--green)}
.brand-name{font-family:"Krona One",sans-serif;font-size:24px;color:var(--ink);line-height:1.1;text-transform:uppercase}
.header-phone{right:170px;top:38px;display:flex;align-items:center;gap:12px;color:var(--blue);font-size:19px}
.header-phone svg{width:28px;height:28px}

.nav{left:0;top:111px;width:1200px;height:39px;background:var(--blue)}
.nav ul{list-style:none;display:flex;margin-left:173px;height:100%}
.nav li{color:var(--white);font-size:14px;display:flex;align-items:center;justify-content:center;border-right:1px solid rgba(255,255,255,.25);height:100%}
.nav li.active{background:var(--orange)}

/* hero */
.hero{left:0;top:150px;width:1200px;height:428px}
.hero-photo{position:absolute;inset:0;background:
  radial-gradient(ellipse 380px 300px at 240px 230px,#f2efea 0%,rgba(242,239,234,0) 100%),
  linear-gradient(90deg,#e9ecef 0%,#d3dae1 35%,#9fb0c2 62%,#7f93a9 100%)}
.hero-copy{position:absolute;left:590px;top:146px;color:var(--white)}
.hero-copy p{font-family:"Krona One",sans-serif;font-size:14px;line-height:1.4;text-transform:uppercase}
.hero-copy h2{font-size:19px;margin-top:6px}
.btn{display:inline-flex;align-items:center;gap:8px;background:var(--orange);color:var(--white);font-weight:500}
.hero-copy .btn{margin-top:12px;padding:7px 14px;font-size:20px;font-weight:700}
.slider-arrow{width:38px;height:38px;border-radius:50%;background:rgba(255,255,255,.7);top:195px;display:flex;align-items:center;justify-content:center}

/* feature band */
.feature{top:578px;height:207px}
.feature h3{font-size:20px;color:var(--white)}
.feature p{font-size:12.5px;color:var(--white);line-height:1.4;margin-top:14px;width:220px}
.feature .btn{font-size:12px;padding:7px 14px;margin-top:18px;font-weight:400}
.photo{top:578px;height:207px}

/* welcome */
.welcome{left:220px;top:825px;width:760px;text-align:center}
.welcome h1{font-size:25px;color:var(--ink)}
.welcome p{font-size:12.5px;line-height:1.45;color:#333;margin-top:16px}
.btn-outline{display:inline-block;margin-top:22px;border:2px solid var(--orange-light);border-radius:4px;padding:8px 10px;font-size:12px;color:#333}

/* contract labeling */
.contract-intro{left:173px;top:1082px;width:360px}
.contract-intro h2{font-size:24px;line-height:1.3;color:var(--ink)}
.contract-intro p{font-size:12px;line-height:1.5;color:#8a8a8a;margin-top:18px}
.link{color:var(--blue);font-size:13px;margin-top:12px;display:block}
.service-tile{top:1089px;width:138px;height:240px}
.service-tile .tile-top{height:98px;display:flex;align-items:center;justify-content:center}
.service-tile .tile-body{height:142px;color:var(--white);font-size:14px;line-height:1.25;text-align:center;padding:22px 14px}

/* what band */
.what{left:0;top:1392px;width:1200px;height:202px;background:linear-gradient(90deg,#5e5e5e,#7a7a7a 50%,#5a5a5a)}
.what .big{left:171px;top:56px;font-family:"Krona One",sans-serif;font-size:74px;color:var(--white)}
.what .mid{left:485px;top:82px;font-family:"Krona One",sans-serif;font-size:25px;line-height:1.05;color:var(--white)}
.what .small{left:608px;top:90px;font-family:"Krona One",sans-serif;font-size:19px;line-height:1.2;color:var(--white)}
.what .btn{left:910px;top:90px;padding:8px 14px;font-size:17px;border-radius:3px;font-weight:700}

/* latest offering */
.offering-title{left:0;top:1640px;width:1200px;text-align:center;font-size:22px;color:var(--ink)}
.card{top:1697px;width:192px;height:309px;border:2px solid #ddd;padding:10px}
.card-photo{height:145px}
.card h4{font-size:13px;font-weight:700;color:var(--ink);text-align:center;margin-top:10px;text-transform:uppercase}
.card h4.active{color:var(--blue)}
.card p{font-size:12px;line-height:1.3;color:#555;margin-top:12px}

/* footer */
.footer{left:0;top:2058px;width:1200px;height:192px;background:var(--footer)}
.footer h3{font-size:15px;color:var(--white)}
.contact-line{display:flex;gap:14px;color:#ddd;font-size:12px;line-height:1.4;margin-top:14px;align-items:flex-start}
.contact-line svg{width:14px;height:14px;flex:none;margin-top:2px}
.location{left:397px;top:96px;width:60px;height:60px;background:var(--green);color:var(--white);font-size:11px;display:flex;flex-direction:column;align-items:center;justify-content:center;gap:4px}
.footer-mark{left:548px;top:18px;width:104px;height:104px;border-radius:50%;background:#3a3a3a}
.social{left:510px;top:148px;display:flex;gap:22px}
.social span{width:20px;height:20px;border-radius:50%;background:var(--white)}
.field{width:143px;height:32px;background:var(--field);color:#999;font-size:11px;padding:9px 10px;margin-bottom:4px}
.message{left:883px;top:38px;width:146px;height:102px;background:var(--field);color:#999;font-size:11px;padding:9px 10px}
.submit{left:731px;top:142px;padding:6px 10px;font-size:12px;font-weight:700;border-radius:3px}
.copyright{left:0;top:2250px;width:1200px;height:54px;background:var(--blue);color:var(--white);font-size:11px;display:flex;align-items:center;justify-content:center}
</style>
</head>
<body>

<header>
  <div class="brand abs">
    <span class="brand-dot"></span>
    <span class="brand-name">Meridane Works<br>Inc.</span>
  </div>
  <div class="header-phone abs">
    <svg viewBox="0 0 28 28"><circle cx="14" cy="14" r="12" fill="none" stroke="#ff7a00" stroke-width="2"/><path d="M10 8c-1 1-1 3 1 6s4 5 6 5c1 0 2-1 2-2l-2-2-2 1c-1-1-2-2-3-4l1-2-2-2z" fill="#ff7a00"/></svg>
    +0800 555 0142
  </div>
</header>

<nav class="nav abs">
  <ul>
    <li class="active" style="width:105px">Home</li>
    <li style="width:125px">About us</li>
    <li style="width:120px">Services</li>
    <li style="width:125px">Products</li>
    <li style="width:136px">User Support</li>
    <li style="width:99px">Blog</li>
    <li style="width:144px;border-right:0">Contact Us</li>
  </ul>
</nav>

<section class="hero abs">
  <div class="hero-photo" role="img" aria-label="Laboratory scene with a scientist using a tablet and a pipette dropping into a glass beaker"></div>
  <div class="slider-arrow abs" style="left:36px"><svg width="14" height="14" viewBox="0 0 14 14"><path d="M9 2 4 7l5 5" fill="none" stroke="#555" stroke-width="2"/></svg></div>
  <div class="slider-arrow abs" style="right:36px"><svg width="14" height="14" viewBox="0 0 14 14"><path d="M5 2l5 5-5 5" fill="none" stroke="#555" stroke-width="2"/></svg></div>
  <div class="hero-copy">
    <p>We are focused on the needs of those<br>individuals involved with</p>
    <h2>Clinical trial materials</h2>
    <span class="btn">Click here to view more <svg width="14" height="14" viewBox="0 0 14 14"><circle cx="7" cy="7" r="6" fill="none" stroke="#fff" stroke-width="1.6"/><path d="M6 4l3 3-3 3" fill="none" stroke="#fff" stroke-width="1.6"/></svg></span>
  </div>
</section>

<section>
  <div class="feature abs" style="left:0;width:428px;background:var(--green);padding:26px 0 0 190px">
    <h3>Our Products</h3>
    <p>Proin ullamcorper at odio ullamcorper fermentum. Fusce rhoncus nunc eu risus egestas dapibus. Suspendisse at erat id est aliquam vestibulum eu quis tellus. Nullam ornare a nisl eu porta.</p>
    <span class="btn">View more »</span>
  </div>
  <div class="photo abs" style="left:428px;width:158px;background:linear-gradient(140deg,#e8edf2 0%,#9fc0e0 30%,#3d6fa8 60%,#c4ccd4 100%)" role="img" aria-label="Gloved hand holding laboratory test tubes"></div>
  <div class="photo abs" style="left:616px;width:154px;background:linear-gradient(135deg,#2f6aa3 0%,#7fa9cc 45%,#eef3f7 75%,#c8d6e2 100%)" role="img" aria-label="Technician in a face mask and protective cap"></div>
  <div class="feature abs" style="left:770px;width:430px;background:var(--blue);padding:26px 0 0 22px">
    <h3>Our Services</h3>
    <p>Proin ullamcorper at odio ullamcorper fermentum. Fusce rhoncus nunc eu risus egestas dapibus. Suspendisse at erat id est aliquam vestibulum eu quis tellus. Nullam ornare a nisl eu porta.</p>
    <span class="btn">View more »</span>
  </div>
</section>

<section class="welcome abs">
  <h1>Welcome to Meridane Works Inc.</h1>
  <p>Vestibulum consectetur, neque sit amet ultricies tempus, eros neque tempor mi, at volutpat mauris tortor sit amet nulla. Nullam ut hendrerit risus. Donec imperdiet velit et elementum hendrerit. Proin ullamcorper at odio ullamcorper fermentum. Fusce rhoncus nunc eu risus egestas dapibus. Suspendisse at erat id est aliquam vestibulum eu quis tellus. Nullam ornare a nisl eu porta. Vivamus eu mollis tellus, ac tincidunt nisl. Phasellus vel est sapien. Integer nec nulla sit amet nunc euismod eleifend. Duis vitae quam tincidunt massa semper mattis.</p>
  <p>Vestibulum ac purus est. Phasellus quis ligula nisi. Ut pharetra non tortor at vehicula. Aenean ultrices sagittis est, vel mattis dolor posuere eu. Nunc pulvinar, leo ut feugiat luctus, urna augue iaculis lacus,</p>
  <span class="btn-outline">View more »</span>
</section>

<section>
  <div class="contract-intro abs">
    <h2>Our Contract<br>Labeling Services</h2>
    <p>Nullam ex turpis, sodales vitae pretium at, scelerisque quis nulla. Aliquam erat volutpat. Proin molestie justo vel ultrices ultrices. Phasellus ullamcorper magna fermentum metus commodo, eu ultrices lacus</p>
    <p>Quisque blandit ex tempor, ultrices elit ac, faucibus ex. Vestibulum sagittis arcu enim. Pellentesque habitant morbi tristique senectus et netus et malesuada fames ac turpis egestas.</p>
    <span class="link">View more »</span>
  </div>
  <div class="service-tile abs" style="left:560px">
    <div class="tile-top" style="background:var(--orange)"><svg width="36" height="36" viewBox="0 0 36 36"><path d="M9 6h17v22H11a2 2 0 0 1-2-2z" fill="none" stroke="#fff" stroke-width="2.5"/><path d="M9 26a2 2 0 0 1 2-2h15M13 11h9M13 15h9" stroke="#fff" stroke-width="2.5" fill="none"/></svg></div>
    <div class="tile-body" style="background:var(--orange-light)">Fusce rhoncus nunc eu risus egestas dapibus. Suspendisse at erat id est</div>
  </div>
  <div class="service-tile abs" style="left:726px">
    <div class="tile-top" style="background:var(--green)"><svg width="40" height="36" viewBox="0 0 40 36"><path d="M6 30C6 14 18 6 34 6c0 16-10 24-22 22M6 30c6-8 12-12 20-16" fill="none" stroke="#fff" stroke-width="2.5"/></svg></div>
    <div class="tile-body" style="background:var(--green-light)">Fusce rhoncus nunc eu risus egestas dapibus. Suspendisse at erat id est</div>
  </div>
  <div class="service-tile abs" style="left:891px">
    <div class="tile-top" style="background:var(--blue)"><svg width="38" height="38" viewBox="0 0 38 38"><path d="M4 18a15 13 0 0 1 30 0z" fill="#fff"/><path d="M19 5v25a3 3 0 0 1-6 0" fill="none" stroke="#fff" stroke-width="2.5"/></svg></div>
    <div class="tile-body" style="background:var(--blue-light)">Fusce rhoncus nunc eu risus egestas dapibus. Suspendisse at erat id est</div>
  </div>
</section>

<section class="what abs" role="img" aria-label="Dimmed production floor with labeling machinery behind the call to action">
  <span class="big abs">WHAT</span>
  <span class="mid abs">YOU<br>NEED</span>
  <span class="small abs">TO KNOW ABOUT<br>MERIDANE WORKS</span>
  <span class="btn abs">View more <svg width="16" height="16" viewBox="0 0 16 16"><circle cx="8" cy="8" r="7" fill="#fff"/><path d="M7 5l3 3-3 3" fill="none" stroke="#ff7a00" stroke-width="1.8"/></svg></span>
</section>

<h2 class="offering-title abs">Latest Offering</h2>
<section>
  <article class="card abs" style="left:171px">
    <div class="card-photo" style="background:linear-gradient(135deg,#5a5a5a,#3a3a3a)" role="img" aria-label="Dark textured panel with expand arrows"><svg width="170" height="145" viewBox="0 0 170 145"><path d="M73 82 98 57M90 57h8v8M81 82h-8v-8" fill="none" stroke="#fff" stroke-width="3"/></svg></div>
    <h4 class="active">Curabir commo sapien</h4>
    <p>Etiam ultricies commodo sap ien, quis auctor dolor faucibus quis. Ut at pretium quam. Morb sapien justo ultrices eget sap ien ut,<br>Quisque gravida, nisl sit amet vulputate tincidunt</p>
  </article>
  <article class="card abs" style="left:394px">
    <div class="card-photo" style="background:linear-gradient(135deg,#f1f3f5 0%,#b9c9da 40%,#6e8cab 70%,#eef1f4 100%)" role="img" aria-label="Scientists working at a laboratory bench"></div>
    <h4>Curabir commo sapien</h4>
    <p>Etiam ultricies commodo sap ien, quis auctor dolor faucibus quis. Ut at pretium quam. Morb sapien justo ultrices eget sap ien ut,<br>Quisque gravida, nisl sit amet vulputate tincidunt</p>
  </article>
  <article class="card abs" style="left:616px">
    <div class="card-photo" style="background:linear-gradient(135deg,#1d3a5e,#4f7fae 50%,#c9d4de 80%,#1f3147)" role="img" aria-label="Researcher operating laboratory analysis equipment"></div>
    <h4>Curabir commo sapien</h4>
    <p>Etiam ultricies commodo sap ien, quis auctor dolor faucibus quis. Ut at pretium quam. Morb sapien justo ultrices eget sap ien ut,<br>Quisque gravida, nisl sit amet vulputate tincidunt</p>
  </article>
  <article class="card abs" style="left:839px">
    <div class="card-photo" style="background:linear-gradient(180deg,#f6f8fa,#dfe6ee 45%,#b3c1d0 75%,#8fa1b5)" role="img" aria-label="Clean room with automated production machines"></div>
    <h4>Curabir commo sapien</h4>
    <p>Etiam ultricies commodo sap ien, quis auctor dolor faucibus quis. Ut at pretium quam. Morb sapien justo ultrices eget sap ien ut,<br>Quisque gravida, nisl sit amet vulputate tincidunt</p>
  </article>
</section>

<footer class="footer abs">
  <div class="abs" style="left:177px;top:28px;width:340px">
    <h3>Get in touch</h3>
    <div class="contact-line" style="margin-top:24px"><svg viewBox="0 0 14 14"><path d="M1 7 7 1l6 6h-2v6H9V9H5v4H3V7z" fill="#fff"/></svg><span>52, Etiam sit amet magna nec quam venen atis<br>veh icula ut sed nisl.</span></div>
    <div class="contact-line"><svg viewBox="0 0 14 14"><path d="M3 1c-2 2-1 5 2 8s6 4 8 2l-2-3-2 1C7 8 6 7 5 5l1-2z" fill="#fff"/></svg><span>+0800 555 0142</span></div>
    <div class="contact-line"><svg viewBox="0 0 14 14"><rect x="1" y="3" width="12" height="8" fill="#fff"/><path d="M1 3l6 5 6-5" fill="none" stroke="#0b0b0b" stroke-width="1.2"/></svg><span>info@meridwork.example</span></div>
  </div>
  <div class="location abs"><svg width="20" height="26" viewBox="0 0 20 26"><path d="M10 1a8 8 0 0 0-8 8c0 6 8 16 8 16s8-10 8-16a8 8 0 0 0-8-8z" fill="#fff"/><circle cx="10" cy="9" r="3" fill="#6cbf14"/></svg>Location</div>
  <div class="footer-mark abs"></div>
  <div class="social abs" aria-label="Social links"><span></span><span></span><span></span><span></span></div>
  <form class="abs" style="left:731px;top:10px">
    <div class="field">Name</div>
    <div class="field">Email</div>
    <div class="field">Phone</div>
  </form>
  <div class="message abs">Message</div>
  <span class="btn submit abs">Submit <svg width="12" height="12" viewBox="0 0 12 12"><circle cx="6" cy="6" r="5.5" fill="#fff"/><path d="M5 3.5 7.5 6 5 8.5" fill="none" stroke="#ff7a00" stroke-width="1.5"/></svg></span>
</footer>
<div class="copyright abs">Copyright © 2014</div>

</body>
</html>
```